Media Browser and player web application

I need to redesign a web application that enables to browse a media server (Tellavo) contents (images, audio, video) and play it in a web player.

Current implementation of the application can be seen at: http://www.tellavohub.example/content/demonstration-tellavo-pro-online-media-browser

This refresh is aiming to:
1) make the application simpler, based on typology (think Windows Metro style, VidSpire, Flickora); a simple fan concept is here: http://dex.lomarquin.example/tellavo/
2) make the application work on desktop as well as touch screen devices (ie no hover functionality, no pagination, large touch controls)
3) fast (remove unnecessary animations)
4) design with the app being responsive in mind

The attached UX designs show the basic flows in the application. Please note that the placement of controls (for example) is not set in stone and I welcome your input on the layout.

Ideally the default theme will be dark. Items' thumbnails will be square place holders, with images fit in them depending on the item icons' aspect ratio.

Also attaching the product's logo (Tellavo) and icon. The web application's name is ClipRover (or Tellavo ClipRover), so it should be included in the design (the UX designs include place holder Tellavo logo in the left top corner).

The main categories for each file type are (you will have to provide an icon for each of these):
- Audio: Albums, Artists, Album artists, Folders, Genres, Composers, Titles, Random music, Random albums, Last listened, Playlists, Online
- Image: Albums, Folders, Year, Month, Playlists, Online
- Video: Titles, Movies, Series, Folders, Last viewed, Last added, Genres, Actors, Directors, Producers, Release years, Playlists, Online
Updates

Target Market(s)

Mostly tech enthusiasts who want to stream their media over the internet to their devices.

Industry/Entity Type

Artists

Requirements
Must have
• Designs for all the provided UX designs
Touch-friendly web application design
High-res (Retina) assets
Light, type based Metro-like design
Nice to have
• Responsive web version
Dark and Light theme switching.
Should not have
• Chrome
Heavy graphics (eg backgrounds) that take time to load

```html
<!DOCTYPE html>
<html lang="en">
<head>
<meta charset="utf-8">
<title>ClipRover – Video</title>
<link href="https://fonts.googleapis.com/css2?family=Open+Sans:wght@300;400;600&display=swap" rel="stylesheet">
<style>
  :root {
    --bar-black: #151515;
    --stage-grey: #4e4c4d;
    --tile-deep: #3bb5e8;
    --tile-soft: #6dcdf2;
    --ink-white: #ffffff;
    --crumb-grey: #a9a9a9;
    --accent-orange: #f5a11c;
    --accent-red: #e8343c;
    --accent-blue: #3bb5e8;
    --control-grey: #3a3a3a;
    --avatar-red: #c8322b;
    --scroll-track: #cfcfcf;
  }
  * { box-sizing: border-box; margin: 0; padding: 0; }
  html, body { width: 1200px; height: 727px; overflow: hidden; background: var(--stage-grey); }
  body { font-family: "Open Sans", sans-serif; color: var(--ink-white); position: relative; }

  .top-bar { position: absolute; left: 0; top: 0; width: 1200px; height: 82px; background: var(--bar-black); }
  .app-name { position: absolute; left: 30px; top: 25px; font-size: 23px; font-weight: 300; letter-spacing: -0.3px; }
  .media-nav a { position: absolute; top: 33px; font-size: 13px; color: var(--ink-white); text-decoration: none; display: flex; align-items: center; gap: 7px; }
  .media-nav svg { width: 18px; height: 16px; }
  .nav-images { left: 244px; }
  .nav-audio { left: 360px; }
  .nav-video { left: 464px; }
  .search-field { position: absolute; left: 604px; top: 28px; width: 143px; height: 26px; border: 1px solid #3d3d3d; border-radius: 13px; background: #0d0d0d; }
  .search-field svg { position: absolute; right: 8px; top: 6px; width: 13px; height: 13px; }
  .tool-button { position: absolute; top: 29px; width: 25px; height: 24px; background: var(--control-grey); border-radius: 2px; }
  .tool-button svg { position: absolute; left: 5px; top: 4px; width: 15px; height: 15px; }
  .theme-toggle { left: 824px; }
  .settings-button { left: 858px; }
  .user-avatar { position: absolute; left: 1043px; top: 20px; width: 46px; height: 43px; background: linear-gradient(135deg, var(--avatar-red), #8e2520); }
  .user-name { position: absolute; left: 1104px; top: 33px; font-size: 12.5px; }

  .section-bar { position: absolute; left: 0; top: 82px; width: 1200px; height: 55px; background: var(--ink-white); }
  .section-title { position: absolute; left: 0; top: 0; width: 193px; height: 55px; background: var(--tile-deep); }
  .section-title h1 { position: absolute; left: 32px; top: 6px; font-size: 30px; font-weight: 300; }
  .section-title svg { position: absolute; left: 174px; top: 22px; width: 12px; height: 12px; }
  .breadcrumb { position: absolute; left: 243px; top: 20px; font-size: 12px; color: var(--crumb-grey); }
  .breadcrumb span { text-decoration: underline; }
  .breadcrumb i { font-style: normal; margin: 0 10px; }
  .queue-control { position: absolute; left: 1136px; top: 8px; width: 34px; text-align: center; color: #999; font-size: 8px; }
  .queue-control svg { width: 30px; height: 30px; display: block; margin: 0 auto 1px; }

  .category-tile { position: absolute; width: 163px; height: 163px; }
  .tile-deep { background: var(--tile-deep); }
  .tile-soft { background: var(--tile-soft); }
  .category-tile svg { position: absolute; left: 39px; top: 20px; width: 85px; height: 85px; fill: var(--ink-white); }
  .category-tile span { position: absolute; left: 0; width: 100%; top: 110px; text-align: center; font-size: 20.5px; }

  .scroll-rail { position: absolute; left: 1178px; top: 165px; width: 15px; height: 416px; border-radius: 7px; background: var(--scroll-track); }
  .scroll-thumb { position: absolute; left: 1180px; top: 196px; width: 11px; height: 134px; border-radius: 5px; background: var(--ink-white); }
</style>
</head>
<body>
<header class="top-bar">
  <div class="app-name">ClipRover</div>
  <nav class="media-nav">
    <a class="nav-images" href="#"><svg viewBox="0 0 18 16"><rect x="1" y="1" width="16" height="14" fill="none" stroke="var(--accent-orange)" stroke-width="2"/><circle cx="6" cy="6" r="2" fill="var(--accent-orange)"/><path d="M3 13l4-4 3 3 2-2 3 3z" fill="var(--accent-orange)"/></svg>IMAGES</a>
    <a class="nav-audio" href="#"><svg viewBox="0 0 18 16"><path d="M6 2l10-2v11.5a2.5 2 0 1 1-2-2V3.5l-6 1.2v8.8a2.5 2 0 1 1-2-2z" fill="var(--accent-red)"/></svg>AUDIO</a>
    <a class="nav-video" href="#"><svg viewBox="0 0 20 16"><circle cx="4" cy="4" r="3" fill="var(--accent-blue)"/><circle cx="10" cy="4" r="3" fill="var(--accent-blue)"/><rect x="1" y="7" width="13" height="8" fill="var(--accent-blue)"/><path d="M14 10l5-3v8l-5-3z" fill="var(--accent-blue)"/></svg>VIDEO</a>
  </nav>
  <div class="search-field"><svg viewBox="0 0 13 13"><circle cx="5" cy="5" r="3.8" fill="none" stroke="#fff" stroke-width="1.8"/><path d="M8 8l4 4" stroke="#fff" stroke-width="2"/></svg></div>
  <div class="tool-button theme-toggle"><svg viewBox="0 0 15 15"><circle cx="7.5" cy="7.5" r="2.6" fill="none" stroke="#aaa" stroke-width="1.2"/><path d="M7.5 1v2M7.5 12v2M1 7.5h2M12 7.5h2M3 3l1.4 1.4M10.6 10.6L12 12M3 12l1.4-1.4M10.6 4.4L12 3" stroke="#aaa" stroke-width="1.2"/></svg></div>
  <div class="tool-button settings-button"><svg viewBox="0 0 15 15"><circle cx="7.5" cy="7.5" r="4.5" fill="#aaa"/><path d="M7.5 1v13M1 7.5h13M3 3l9 9M3 12l9-9" stroke="#aaa" stroke-width="2.4"/><circle cx="7.5" cy="7.5" r="1.8" fill="var(--control-grey)"/></svg></div>
  <div class="user-avatar" role="img" aria-label="User profile photo"></div>
  <div class="user-name">DAN MORELL</div>
</header>

<section class="section-bar">
  <div class="section-title"><h1>VIDEO</h1><svg viewBox="0 0 12 12"><circle cx="6" cy="6" r="6" fill="#fff"/><path d="M3 6h5M6 3.5L8.5 6 6 8.5" stroke="var(--tile-deep)" stroke-width="1.6" fill="none"/></svg></div>
  <div class="breadcrumb"><span>Home</span><i>›</i><span>Video</span></div>
  <div class="queue-control"><svg viewBox="0 0 30 30"><circle cx="15" cy="15" r="13.5" fill="none" stroke="#999" stroke-width="1.3"/><rect x="10" y="9" width="10" height="12" rx="1" fill="none" stroke="#999" stroke-width="1.3"/><path d="M12 13h6M12 15.5h6M12 18h6" stroke="#999"/></svg>Queue</div>
</section>

<main class="category-grid">
  <div class="category-tile tile-deep" style="left:30px;top:167px"><svg viewBox="0 0 80 80"><rect x="30" y="2" width="10" height="76"/><path d="M4 10h56l12 13-12 13H4z"/><rect x="12" y="20" width="30" height="6" fill="var(--tile-deep)"/><path d="M18 42h44v16H18l-8-8z"/></svg><span>Titles</span></div>
  <div class="category-tile tile-soft" style="left:225px;top:167px"><svg viewBox="0 0 80 80"><path d="M2 12h76v56H2zM6 16v8h6v-8zm0 14v8h6v-8zm0 14v8h6v-8zm0 14v6h6v-6zM68 16v8h6v-8zm0 14v8h6v-8zm0 14v8h6v-8zm0 14v6h6v-6zM16 16v48h48V16z" fill-rule="evenodd"/><path d="M32 26l18 14-18 14z"/></svg></div>
  <div class="category-tile tile-deep" style="left:420px;top:167px"><svg viewBox="0 0 80 80"><text x="40" y="58" text-anchor="middle" font-family="Open Sans, sans-serif" font-weight="600" font-size="40" fill="#fff">1<tspan dy="-12">2</tspan><tspan dy="12">3</tspan></text></svg><span>Series</span></div>
  <div class="category-tile tile-soft" style="left:614px;top:167px"><svg viewBox="0 0 80 80"><path d="M4 8h24l6 6h30v10H14L4 70z"/><path d="M16 28h62L66 72H4z"/></svg><span>Folders</span></div>
  <div class="category-tile tile-deep" style="left:810px;top:167px"><svg viewBox="0 0 80 80"><path d="M2 40C14 22 28 16 40 16s26 6 38 24C66 58 52 64 40 64S14 58 2 40z"/><circle cx="40" cy="40" r="16" fill="var(--tile-deep)"/><circle cx="40" cy="40" r="11"/></svg><span>Last Viewed</span></div>
  <div class="category-tile tile-soft" style="left:1005px;top:167px"><svg viewBox="0 0 80 80"><path d="M44 2l30 30-6 4-4-2-14 14 2 14-6 6-14-16L6 78l-2-2 26-26L14 36l6-6 14 2 14-14-2-4z"/></svg><span>Last Added</span></div>

  <div class="category-tile tile-soft" style="left:30px;top:360px"><svg viewBox="0 0 80 80"><rect x="4" y="8" width="16" height="16"/><rect x="4" y="32" width="16" height="16"/><rect x="4" y="56" width="16" height="16"/><rect x="28" y="12" width="48" height="8"/><rect x="28" y="36" width="48" height="8"/><rect x="28" y="60" width="48" height="8"/></svg><span>Genres</span></div>
  <div class="category-tile tile-deep" style="left:225px;top:360px"><svg viewBox="0 0 80 80"><circle cx="40" cy="40" r="34" fill="none" stroke="#fff" stroke-width="7"/><path d="M40 20l6 13 14 1-11 9 4 14-13-8-13 8 4-14-11-9 14-1z"/></svg><span>Actors</span></div>
  <div class="category-tile tile-soft" style="left:420px;top:360px"><svg viewBox="0 0 80 80"><rect x="16" y="4" width="48" height="18"/><rect x="14" y="4" width="4" height="30"/><rect x="62" y="4" width="4" height="30"/><rect x="12" y="30" width="56" height="6"/><path d="M20 36h8l34 40h-8zM52 36h8L26 76h-8z"/><path d="M40 8l2 4 4 .5-3 3 1 4-4-2-4 2 1-4-3-3 4-.5z" fill="var(--tile-soft)"/></svg><span>Directors</span></div>
  <div class="category-tile tile-deep" style="left:614px;top:360px"><svg viewBox="0 0 80 80"><path d="M6 20L70 4l3 11L9 31z"/><path d="M8 36h66v38H8z"/><path d="M10 40h60v6H10z" fill="var(--tile-deep)"/></svg><span>Producers</span></div>
  <div class="category-tile tile-soft" style="left:810px;top:360px"><svg viewBox="0 0 80 80"><rect x="2" y="4" width="76" height="8"/><rect x="2" y="4" width="8" height="70"/><rect x="70" y="4" width="8" height="70"/><path d="M10 12h22c-4 20-10 40-22 56zM70 12H48c4 20 10 40 22 56z"/><rect x="2" y="68" width="76" height="6"/></svg><span>Release Years</span></div>
  <div class="category-tile tile-deep" style="left:1005px;top:360px"><svg viewBox="0 0 80 80"><circle cx="40" cy="40" r="36"/><circle cx="40" cy="40" r="30" fill="var(--tile-deep)"/><circle cx="40" cy="40" r="27"/><circle cx="40" cy="40" r="9" fill="var(--tile-deep)"/><circle cx="40" cy="40" r="4"/><path d="M26 18a26 26 0 0 0-10 12" stroke="var(--tile-deep)" stroke-width="3" fill="none"/></svg></div>

  <div class="category-tile tile-deep" style="left:30px;top:554px"><svg viewBox="0 0 80 80"><path d="M2 6h76v54H2zM8 12v42h64V12z" fill-rule="evenodd"/><rect x="34" y="60" width="12" height="10"/><rect x="20" y="70" width="40" height="5"/></svg><span>Online</span></div>
</main>

<div class="scroll-rail"></div>
<div class="scroll-thumb"></div>
</body>
</html>
```